Presentation folder for holding wedding cake literature

We need to have a front cover design as well as a back cover design for a presentation folder to hold literature for a bakery who sells a lot of wedding cakes.

We have uploaded a couple copies of ideas that we like. They are for demonstrative purposes only.

The text on the front cover needs to be:
-The Frosting Parlour-
-Designing, baking and decorating perfect wedding cakes...Guaranteed!

On the back cover it needs to say:
-Serving VELVETcrumb cakes and a "Silver Ribbon" Experience-

In addition the back cover must contain the "Silver Ribbon Baker" logo.

We will only supply photos if necessary. We would rather have you choose them.

We are open to any colors as long as they are soft.

For a reference of the client, go to http://www.brindlefrostingparlour.example

Target Market(s)

The target market is primarily women ages 25-40.

Industry/Entity Type

Wedding

Requirements
Must have
• Must have priorities are listed in the brief.
Nice to have
• Fonts should be a combination of "script" and one or more complementary styles.

Colors should be either a soft blue, pinkish tone or lavender tone. Mixing any of the colors with a light gray would be acceptable as well.
Should not have
• No dark colors such as black, red, purple, green or orange.

```html
<!DOCTYPE html>
<html lang="en">
<head>
<meta charset="utf-8">
<title>The Frosting Parlour – Presentation Folder</title>
<link rel="stylesheet" href="https://fonts.googleapis.com/css2?family=Kaushan+Script&family=Tinos&display=swap">
<style>
  :root {
    --backdrop: #ebe8e4;
    --panel-edge: #b7c3cc;
    --panel-glow: #eef2f5;
    --panel-light: #ffffff;
    --accent-blue: #9fd6e2;
    --divider: #c4c4c4;
    --ink: #4a4a4a;
    --ink-soft: #5e5e5e;
    --brand-gold: #c9972f;
    --brand-blue: #2f8fc6;
  }
  html, body {
    margin: 0;
    padding: 0;
    width: 1200px;
    height: 1015px;
    overflow: hidden;
    background: var(--backdrop);
  }
  .canvas {
    position: relative;
    width: 1200px;
    height: 1015px;
  }
  .folder-spread {
    position: absolute;
    left: 20px;
    top: 120px;
    width: 1160px;
    height: 774px;
    box-shadow: 0 6px 18px rgba(0,0,0,0.18);
  }
  .cover-title {
    font-family: "Kaushan Script", cursive;
    font-size: 44px;
    fill: var(--ink);
  }
  .cover-tagline {
    font-family: "Tinos", serif;
    font-size: 21px;
    fill: var(--ink-soft);
  }
  .brand-name {
    font-family: "Tinos", serif;
    font-size: 33px;
    fill: var(--brand-gold);
  }
  .back-tagline {
    font-family: "Tinos", serif;
    font-size: 15px;
    fill: var(--ink-soft);
  }
</style>
</head>
<body>
<main class="canvas">
  <svg class="folder-spread" viewBox="0 0 917 612" xmlns="http://www.w3.org/2000/svg">
    <defs>
      <radialGradient id="panel-glow-left" cx="0.45" cy="0.5" r="0.75">
        <stop offset="0" stop-color="var(--panel-glow)"/>
        <stop offset="1" stop-color="var(--panel-edge)"/>
      </radialGradient>
      <radialGradient id="panel-glow-right" cx="0.55" cy="0.5" r="0.75">
        <stop offset="0" stop-color="var(--panel-glow)"/>
        <stop offset="1" stop-color="var(--panel-edge)"/>
      </radialGradient>
      <linearGradient id="photo-berry" x1="0" y1="0" x2="1" y2="1">
        <stop offset="0" stop-color="#c9a08a"/><stop offset="1" stop-color="#e9dccd"/>
      </linearGradient>
      <linearGradient id="photo-garden" x1="0" y1="0" x2="1" y2="1">
        <stop offset="0" stop-color="#a3ae8e"/><stop offset="1" stop-color="#e4d6d8"/>
      </linearGradient>
      <linearGradient id="photo-bow" x1="0" y1="0" x2="1" y2="1">
        <stop offset="0" stop-color="#9fb0b6"/><stop offset="1" stop-color="#d8eef0"/>
      </linearGradient>
      <linearGradient id="photo-white" x1="0" y1="0" x2="1" y2="1">
        <stop offset="0" stop-color="#f4f1ee"/><stop offset="1" stop-color="#d9d4d0"/>
      </linearGradient>
      <linearGradient id="photo-lace" x1="0" y1="0" x2="1" y2="1">
        <stop offset="0" stop-color="#eeeae6"/><stop offset="1" stop-color="#c8b6b0"/>
      </linearGradient>
      <linearGradient id="photo-cream" x1="0" y1="0" x2="1" y2="1">
        <stop offset="0" stop-color="#d8d2cb"/><stop offset="1" stop-color="#f3f0ec"/>
      </linearGradient>
    </defs>

    <!-- back cover panel -->
    <rect class="side-panel" x="0" y="0" width="260" height="612" fill="url(#panel-glow-left)"/>
    <!-- front cover panel -->
    <rect class="side-panel" x="657" y="0" width="260" height="612" fill="url(#panel-glow-right)"/>

    <!-- inner white flaps with blue sweeps -->
    <path class="flap-accent" d="M243 0 L283 0 Q244 300 238 612 L228 612 Q212 300 243 0 Z" fill="var(--accent-blue)"/>
    <path class="flap-panel" d="M256 0 L458 0 L458 612 L234 612 Q224 300 256 0 Z" fill="var(--panel-light)"/>
    <path class="flap-accent" d="M674 0 L634 0 Q673 300 679 612 L689 612 Q705 300 674 0 Z" fill="var(--accent-blue)"/>
    <path class="flap-panel" d="M661 0 L459 0 L459 612 L683 612 Q693 300 661 0 Z" fill="var(--panel-light)"/>
    <line class="fold-line" x1="458.5" y1="0" x2="458.5" y2="612" stroke="var(--divider)" stroke-width="2"/>

    <!-- back cover photo column -->
    <g class="photo-column">
      <rect role="img" aria-label="Photo: square tiered wedding cake topped with strawberries" x="-72" y="-56" width="144" height="112" fill="url(#photo-berry)" stroke="#fff" stroke-width="1" transform="translate(114 90) rotate(12)"/>
      <rect role="img" aria-label="Photo: couple beside a floral wedding cake in a garden" x="-72" y="-50" width="144" height="100" fill="url(#photo-garden)" transform="translate(112 228) rotate(-7)"/>
      <rect role="img" aria-label="Photo: white fondant cake with a large turquoise bow" x="-72" y="-54" width="144" height="108" fill="url(#photo-bow)" transform="translate(125 370) rotate(-7)"/>
      <rect role="img" aria-label="Photo: white tiered cakes with a couple cake topper" x="-75" y="-52" width="150" height="104" fill="url(#photo-white)" transform="translate(132 522) rotate(-9)"/>
    </g>

    <!-- front cover photo column -->
    <g class="photo-column">
      <rect role="img" aria-label="Photo: lace-piped cake with blush roses" x="-70" y="-52" width="140" height="104" fill="url(#photo-lace)" transform="translate(794 92) rotate(-12)"/>
      <rect role="img" aria-label="Photo: basket-weave white tiered cake" x="-72" y="-50" width="144" height="100" fill="url(#photo-cream)" transform="translate(793 230) rotate(-5)"/>
      <rect role="img" aria-label="Photo: heart-shaped white cake with piped details" x="-70" y="-52" width="140" height="104" fill="url(#photo-white)" transform="translate(806 372) rotate(8)"/>
      <rect role="img" aria-label="Photo: tiered cake with piped rosettes" x="-72" y="-50" width="144" height="100" fill="url(#photo-cream)" transform="translate(810 520) rotate(-10)"/>
    </g>

    <!-- back cover brand -->
    <g class="brand-mark">
      <circle cx="282" cy="306" r="12" fill="var(--brand-blue)"/>
      <text class="brand-name" x="302" y="303">Silver</text>
      <text class="brand-name" x="302" y="338">Ribbon</text>
    </g>

    <!-- back cover message -->
    <g class="back-copy">
      <text class="back-tagline" x="350" y="392" text-anchor="middle">Serving VELVETcrumb cakes</text>
      <text class="back-tagline" x="350" y="414" text-anchor="middle">and a “Silver Ribbon”</text>
      <text class="back-tagline" x="350" y="436" text-anchor="middle">Experience</text>
    </g>

    <!-- front cover copy -->
    <g class="cover-copy">
      <text class="cover-title" x="476" y="152">The</text>
      <text class="cover-title" x="476" y="210">Frosting</text>
      <text class="cover-title" x="476" y="268">Parlour</text>
      <text class="cover-tagline" x="476" y="330">Designing</text>
      <text class="cover-tagline" x="476" y="363">baking and</text>
      <text class="cover-tagline" x="476" y="397">decorating perfect</text>
      <text class="cover-tagline" x="476" y="430">wedding cakes...</text>
      <text class="cover-tagline" x="476" y="464">Guaranteed!</text>
    </g>
  </svg>
</main>
</body>
</html>
```